Business card design for IT consulting company

Looking for a simple, modern, clean business card design.
Open to reworking our existing logo.

Attached is our current business cards which we do not like.
Ideally double sided with something simple on the back.
Rectangle / Horizonal only.
No rounded edges on the card.
White as the dominate color is preferred.

Target Market(s)

clients, legal, oil & gas, medical, professionals

Industry/Entity Type

IT, tech, consulting

Contact Information for Business Card

Name, Title, email, phone, cell, website

Font styles to use
Sans Serif

Requirements
Must have
• Clean design
Should not have
• loud colors or unusual fonts, etc

```html
<!DOCTYPE html>
<html lang="en">
<head>
<meta charset="utf-8">
<title>Nexa Solutions – Business Card</title>
<link href="https://fonts.googleapis.com/css2?family=Arimo:wght@400;700&display=swap" rel="stylesheet">
<style>
  :root {
    --bg: #d9d9db;
    --paper: #fbfbfb;
    --ink: #111111;
    --ink-soft: #333333;
    --navy: #1f2170;
    --red: #e23a4f;
    --yellow: #f2c12e;
    --sky: #3fa9dc;
    --rule: #c9c9c9;
  }
  * { margin: 0; padding: 0; box-sizing: border-box; }
  html, body {
    width: 1200px; height: 799px; overflow: hidden;
    background: var(--bg);
    font-family: "Arimo", Helvetica, Arial, sans-serif;
    color: var(--ink);
  }
  .stage { position: relative; width: 1200px; height: 799px; }
  .card {
    position: absolute; top: 245px;
    width: 540px; height: 309px;
    background: var(--paper);
    box-shadow: 0 6px 18px rgba(0,0,0,0.12);
    overflow: hidden;
  }
  .card--front { left: 40px; }
  .card--back { left: 620px; }

  .brand { display: flex; align-items: center; gap: 12px; }
  .brand__mark { width: 40px; height: 40px; background: var(--navy); flex: none; }
  .brand__name { font-weight: 700; font-size: 28px; letter-spacing: -0.3px; color: var(--ink); white-space: nowrap; }

  .card--front .brand { position: absolute; left: 46px; top: 112px; }
  .divider { position: absolute; left: 300px; top: 92px; width: 1px; height: 82px; background: var(--rule); }

  .contact { position: absolute; left: 322px; top: 86px; }
  .contact__name { font-weight: 700; font-size: 17px; line-height: 1.1; }
  .contact__title { font-size: 11px; color: var(--ink-soft); margin-bottom: 8px; }
  .contact__line { display: flex; align-items: center; gap: 7px; font-size: 12px; line-height: 17px; color: var(--ink-soft); }
  .contact__line svg { width: 11px; height: 11px; flex: none; }

  .accent { position: absolute; left: 0; bottom: 6px; height: 8px; }
  .accent--yellow { left: 0; width: 80px; background: var(--yellow); }
  .accent--red { left: 80px; width: 190px; background: var(--red); }
  .accent--sky { left: 270px; width: 120px; background: var(--sky); }
  .base-band { position: absolute; left: 0; right: 0; bottom: 0; height: 6px; background: var(--navy); }
  .web-band {
    position: absolute; right: 0; bottom: 0; width: 150px; height: 34px;
    background: var(--navy); color: #fff;
    font-size: 12px; display: flex; align-items: center; justify-content: center;
  }

  .card--back .brand { position: absolute; left: 50%; top: 50%; transform: translate(-50%, -50%); gap: 16px; }
  .card--back .brand__mark { width: 62px; height: 62px; }
  .card--back .brand__name { font-size: 44px; }
</style>
</head>
<body>
<main class="stage">
  <section class="card card--front" aria-label="Business card front">
    <div class="brand">
      <span class="brand__mark"></span>
      <span class="brand__name">Nexa Solutions</span>
    </div>
    <div class="divider"></div>
    <div class="contact">
      <p class="contact__name">Daniel Reyes</p>
      <p class="contact__title">IT Consultant</p>
      <p class="contact__line">
        <svg viewBox="0 0 12 12" aria-hidden="true"><path d="M2.5 1h2l1 3-1.3 1a6 6 0 0 0 2.8 2.8l1-1.3 3 1v2a1 1 0 0 1-1 1A9.5 9.5 0 0 1 1.5 2a1 1 0 0 1 1-1z" fill="var(--yellow)"/></svg>
        (800)555-0147
      </p>
      <p class="contact__line">
        <svg viewBox="0 0 12 12" aria-hidden="true"><rect x="3" y="0.8" width="6" height="10.4" rx="1" fill="none" stroke="var(--red)" stroke-width="1.3"/></svg>
        (555) 210-4478
      </p>
      <p class="contact__line">
        <svg viewBox="0 0 12 12" aria-hidden="true"><rect x="0.5" y="2.5" width="11" height="7.5" fill="var(--sky)"/><path d="M0.8 2.8 6 7l5.2-4.2" fill="none" stroke="#fff" stroke-width="1"/></svg>
        daniel.reyes@nexatech.ca
      </p>
    </div>
    <span class="accent accent--yellow"></span>
    <span class="accent accent--red"></span>
    <span class="accent accent--sky"></span>
    <span class="base-band"></span>
    <span class="web-band">www.nexatech.ca</span>
  </section>

  <section class="card card--back" aria-label="Business card back">
    <div class="brand">
      <span class="brand__mark"></span>
      <span class="brand__name">Nexa Solutions</span>
    </div>
  </section>
</main>
</body>
</html>
```